On Demand Digital Interview Lunch and Learn Event Flyer

We are hosting a lunch and learn for prospects to introduce our Digital Interview process - attendees are Human Resource and Hiring Managers.

We need a flyer that we can email and also have printed (large postcard size) to be either mailed out or dropped off at a prospects location. I have included a picture of a Digital Interview to be used on the flyer (people don't get it till they see it) as well as content. Please feel free to rewrite, restructure, the content to produce a good flow.

Return address on the back (the one we would print) is RL Workforce - 2740 Halden Road - Suite 318 - Nashville, TN 37482

Target Market(s)

Business Owners, Human Resource Managers

Industry/Entity Type

Digital

Font styles to use
Sans Serif

Requirements
Must have
• Must be clean and professional with plenty of white space

```html
<!DOCTYPE html>
<html lang="en">
<head>
<meta charset="utf-8">
<title>Digital Interview Lunch and Learn – RL Workforce</title>
<link href="https://fonts.googleapis.com/css2?family=Oswald:wght@500;600&family=Source+Sans+3:wght@400;600&display=swap" rel="stylesheet">
<style>
  :root{
    --red:#d21f2b;
    --red-deep:#a3121c;
    --ink:#111111;
    --bar:#1b1b1b;
    --soft-grey:#c9c9c9;
    --pill:#e4e4e4;
    --paper:#ffffff;
    --page:#e9e9e9;
    --line:#9a9a9a;
  }
  *{box-sizing:border-box;margin:0;padding:0}
  html,body{width:806px;height:1200px;overflow:hidden;background:var(--page)}
  body{position:relative;font-family:"Source Sans 3",Arial,sans-serif}
  .card{position:absolute;left:43px;width:720px;height:465px;background:var(--paper);overflow:hidden;box-shadow:0 2px 8px rgba(0,0,0,.25)}
  .card--front{top:110px}
  .card--back{top:615px}
  .shape{position:absolute;left:0;top:0}
  .display{font-family:"Oswald","Arial Narrow",sans-serif;font-weight:600}

  /* front */
  .headline{position:absolute;left:31px;top:30px;font-size:36px;line-height:44px;color:var(--ink);letter-spacing:.2px}
  .headline em{font-style:normal;color:var(--red)}
  .team-photo{position:absolute;left:360px;top:6px;width:360px;height:190px;background:radial-gradient(ellipse at 55% 45%,#cfc6c0 0%,#e9e6e4 55%,#ffffff 100%)}
  .logo-panel{position:absolute;left:25px;top:185px;width:206px;height:89px;border-radius:6px;background:linear-gradient(180deg,#ffffff,#e2e2e2);display:flex;align-items:center;justify-content:center;gap:8px}
  .logo-panel .dot{width:12px;height:12px;border-radius:50%;background:var(--red)}
  .logo-panel .name{font-family:"Oswald",sans-serif;font-weight:600;font-size:26px;color:var(--red)}
  .intro{position:absolute;left:25px;top:282px;width:311px;font-size:11.6px;line-height:15.6px;color:#fff;text-align:justify}
  .benefits-title{position:absolute;left:466px;top:228px;width:254px;height:23px;background:var(--pill);border-radius:12px 0 0 12px;font-family:"Oswald",sans-serif;font-weight:500;font-size:14px;line-height:23px;color:var(--ink);padding-left:14px}
  .benefits{position:absolute;right:22px;top:262px;list-style:none;text-align:right}
  .benefits li{font-size:11.2px;line-height:21.2px;color:#fff;white-space:nowrap}
  .benefits li::after{content:"";display:inline-block;width:8px;height:8px;border-radius:50%;background:var(--bar);margin-left:9px;vertical-align:middle}
  .rsvp-bar{position:absolute;left:0;bottom:0;width:720px;height:44px;background:var(--bar);font-family:"Oswald",sans-serif;font-weight:500;font-size:19.5px;line-height:44px;color:#fff;text-align:center}
  .rsvp-bar .detail{color:var(--soft-grey)}
  .rsvp-bar strong{font-weight:600}

  /* back */
  .event{position:absolute;left:0;top:30px;width:390px;text-align:center}
  .event .label{display:inline-block;font-size:26px;line-height:32px;color:var(--ink);text-decoration:underline;text-decoration-thickness:2px;text-underline-offset:3px}
  .event .big{font-size:30px;line-height:38px;color:#fff}
  .event .big.muted{color:var(--soft-grey)}
  .event .gap{height:10px}
  .event sup{font-size:14px;vertical-align:14px}
  .purpose-title{position:absolute;left:0;top:287px;width:166px;height:24px;background:var(--pill);border-radius:0 12px 12px 0;font-family:"Oswald",sans-serif;font-weight:500;font-size:14px;line-height:24px;color:var(--ink);padding-left:18px}
  .purpose{position:absolute;left:18px;top:320px;width:225px;font-size:12.6px;line-height:16px;color:#fff}
  .presenter-video{position:absolute;left:205px;top:294px;width:155px;height:128px;background:radial-gradient(ellipse at 50% 40%,#8c6e55 0%,#b56048 45%,#c2303a 100%)}
  .return-address{position:absolute;left:411px;top:23px;font-size:9px;line-height:11px;color:#222;font-style:normal}
  .stamp{position:absolute;left:647px;top:20px;width:49px;height:63px;border:1px solid var(--line)}
  .address-line{position:absolute;left:508px;width:183px;height:1px;background:var(--line)}
  .address-line--1{top:245px}
  .address-line--2{top:276px}
  .address-line--3{top:307px}
</style>
</head>
<body>

<section class="card card--front">
  <div class="team-photo" role="img" aria-label="Photo of five cheering young professionals in business attire"></div>
  <svg class="shape" width="720" height="465" viewBox="0 0 720 465" aria-hidden="true">
    <defs>
      <linearGradient id="frontRed" x1="0" y1="0" x2="0" y2="1">
        <stop offset="0" stop-color="#dc2632"/>
        <stop offset="1" stop-color="#b5151f"/>
      </linearGradient>
    </defs>
    <path d="M0 218 C180 268 330 190 470 178 C580 170 660 186 720 198 L720 214 C650 202 560 190 470 198 C330 210 200 282 0 236 Z" fill="#bdbdbd"/>
    <path d="M0 236 C200 282 330 210 470 198 C560 190 650 202 720 214 L720 421 L0 421 Z" fill="url(#frontRed)"/>
  </svg>
  <h1 class="headline display">How <em>Digital Interviews</em><br>Can Produce Better<br>Candidates</h1>
  <div class="logo-panel"><span class="dot"></span><span class="name">RL Workforce</span></div>
  <p class="intro">On Demand Digital Interviews offer individuals the ability to share their stories and demonstrate their work through video – all on their own time by using a PC, laptop, or Smartphone. More than 60% of interviews take place outside of the normal 9-5 business hours. Learn how Hiring Managers can save time, qualify more candidates, and can get a better overall first impression before setting up a first round interview.</p>
  <div class="benefits-title">Benefits of Digital interviewing include</div>
  <ul class="benefits">
    <li>Lower Recruiting Costs</li>
    <li>Higher Quality Talent Pools</li>
    <li>Screen More Candidates in Less Time</li>
    <li>Schedule First Round Interviews with only Qualified Candidates</li>
    <li>Share with Multiple Hiring Managers</li>
    <li>Reduced Travel Expenses</li>
    <li>On Demand Flexibility</li>
  </ul>
  <div class="rsvp-bar"><strong>RSVP:</strong>&nbsp; <span class="detail">Dana.morrow@rlworkforce.com</span> or call <span class="detail">615 555-0148</span> for more information</div>
</section>

<section class="card card--back">
  <svg class="shape" width="720" height="465" viewBox="0 0 720 465" aria-hidden="true">
    <defs>
      <linearGradient id="backRed" x1="0" y1="0" x2="1" y2="1">
        <stop offset="0" stop-color="#c41b27"/>
        <stop offset=".55" stop-color="#d9303b"/>
        <stop offset="1" stop-color="#b0141e"/>
      </linearGradient>
    </defs>
    <path d="M0 0 L404 0 C428 60 420 160 398 260 C386 320 384 380 382 422 L0 422 Z" fill="#bdbdbd"/>
    <path d="M0 0 L390 0 C414 60 406 160 384 260 C372 320 370 380 368 422 L0 422 Z" fill="url(#backRed)" role="img" aria-label="Faded photo of office colleagues under a red tint"/>
  </svg>
  <div class="event display">
    <div class="label">Where</div>
    <div class="big muted">HALDEN COUNTY</div>
    <div class="big">CHAMBER OF COMMERCE</div>
    <div class="gap"></div>
    <div class="label">When</div>
    <div class="big muted">11:30 - 1:00PM</div>
    <div class="big">WEDNESDAY, AUGUST 24<sup>th</sup></div>
  </div>
  <div class="presenter-video" role="img" aria-label="Still from a digital interview video showing a presenter speaking to camera"></div>
  <div class="purpose-title">Presentation Purpose:</div>
  <p class="purpose">A step-by-step demonstration and an overall introduction to Digital Interviewing and why they have quickly replaced the phone interview and resume.</p>
  <address class="return-address">Return address to:<br>RL Workforce<br>2740 Halden Road<br>Suite 318 - Nashville,<br>TN 37482</address>
  <div class="stamp"></div>
  <div class="address-line address-line--1"></div>
  <div class="address-line address-line--2"></div>
  <div class="address-line address-line--3"></div>
  <div class="rsvp-bar"><strong>RSVP:</strong>&nbsp; <span class="detail">Dana.morrow@rlworkforce.com</span> or call <span class="detail">615 555-0148</span> for more information</div>
</section>

</body>
</html>
```